Sydney law firm, Prestwicks Solicitors, needs a flyer design!

We need a flyer design for our law firm which has been operating in Sydney for over 35 years. We want to send the flyer out to potential clients and also to existing clients to let them know the range of services that we provide. Our corporate colours are white, red and black and we would like these incorporated somewhat. The final design should be clean, modern and professional.

We would like the design to fit a double sided flyer approx. 210mm high x 100mm wide.

Industry/Entity Type

Law Firm

Font styles to use
Serif
Sans Serif

Colors
eb2026
ffffff

Requirements
Must have
• Details needed on the flyer are:
• Prestwicks Solicitors
• 3/82 Carradine Street, Liverpool, NSW 2170
• (02) 9418 3562
• www.prestwickssolicitors-example.com.au
• info@prestwickssolicitors-example.com.au
• Our areas of practice include:
• Property Law
• Conveyancing
• Leases
• Criminal Law
• Family Law
• Litigation and Dispute Resolution
• Company Law
• Wills and Estates
• Powers of Attorney and Guardianship
Should not have
• a picture of scales or a picture of a gavel

```html
<!DOCTYPE html>
<html lang="en">
<head>
<meta charset="utf-8">
<title>Prestwicks Solicitors – Flyer</title>
<link href="https://fonts.googleapis.com/css2?family=Roboto:wght@300;400;500;700&display=swap" rel="stylesheet">
<style>
  :root {
    --red: #eb2026;
    --red-muted: #c8473d;
    --ink: #2b2b2b;
    --grey-text: #6a6a6a;
    --paper: #ffffff;
    --footer-grey: #e6e6e6;
    --stage: #ececec;
  }
  * { box-sizing: border-box; margin: 0; padding: 0; }
  html, body { width: 1200px; height: 800px; overflow: hidden; }
  body {
    background: var(--stage);
    font-family: "Roboto", Arial, sans-serif;
    color: var(--ink);
    position: relative;
  }
  .flyer {
    position: absolute;
    top: 50px;
    width: 490px;
    height: 700px;
    background: var(--paper);
    border-top: 4px solid var(--red);
    border-bottom: 6px solid var(--red);
    box-shadow: 0 6px 24px rgba(0,0,0,0.12);
    overflow: hidden;
  }
  .flyer--back { left: 75px; }
  .flyer--front { left: 635px; }

  /* Shared footer */
  .contact-footer {
    position: absolute;
    left: 0; right: 0; bottom: 0;
    height: 120px;
    background: linear-gradient(180deg, #efefef, var(--footer-grey));
    display: flex;
    justify-content: space-between;
    padding: 24px 32px;
    font-size: 12px;
    line-height: 1.45;
  }
  .contact-footer .firm-name { color: var(--red); font-weight: 700; font-size: 15px; }
  .contact-footer .address { color: var(--ink); }
  .contact-footer .lines { text-align: left; align-self: flex-end; }
  .contact-footer .phone { color: var(--red); font-size: 15px; font-weight: 500; }
  .contact-footer .phone strong { font-weight: 700; }

  /* Back side */
  .practice-heading {
    text-align: center;
    font-size: 22px;
    font-weight: 300;
    letter-spacing: 1px;
    color: var(--ink);
    padding-top: 26px;
  }
  .practice-heading strong { font-weight: 700; }
  .practice-rule {
    width: 400px;
    height: 2px;
    background: var(--red);
    margin: 10px auto 14px;
  }
  .practice-list { list-style: none; text-align: center; padding: 0 36px; }
  .practice-item { margin-bottom: 10px; }
  .practice-item h3 {
    color: var(--red);
    font-size: 15px;
    font-weight: 700;
    text-transform: uppercase;
    letter-spacing: 0.3px;
  }
  .practice-item p {
    color: var(--grey-text);
    font-size: 10.5px;
    line-height: 1.35;
    margin-top: 2px;
  }

  /* Front side */
  .brand-header {
    height: 120px;
    display: flex;
    justify-content: flex-end;
    align-items: center;
    padding-right: 34px;
  }
  .brand-name {
    font-size: 30px;
    font-weight: 400;
    letter-spacing: 3px;
    text-transform: uppercase;
    color: var(--ink);
    text-align: right;
    line-height: 1.05;
  }
  .brand-name span { display: block; font-size: 13px; letter-spacing: 8px; }
  .hero-photo {
    height: 190px;
    background: linear-gradient(115deg, #3a3a3a 0%, #6d6d6d 45%, #b9b9b9 80%, #dcdcdc 100%);
  }
  .hero-band {
    background: var(--red-muted);
    color: #fff;
    text-align: center;
    padding: 16px 20px;
    font-size: 20px;
    font-weight: 300;
    line-height: 1.25;
    text-transform: uppercase;
    letter-spacing: 0.5px;
  }
  .hero-band strong { font-weight: 700; }
  .intro {
    padding: 20px 34px 0;
    text-align: center;
    font-size: 12.5px;
    line-height: 1.5;
    color: var(--ink);
  }
  .intro .tagline { font-weight: 700; margin-top: 8px; }
</style>
</head>
<body>

<section class="flyer flyer--back">
  <h2 class="practice-heading">OUR <strong>AREAS OF PRACTICE</strong></h2>
  <div class="practice-rule"></div>
  <ul class="practice-list">
    <li class="practice-item"><h3>Property Law</h3><p>Advice, Residential and Commercial Property, Property Development, Building Disputes, Easements and Covenants</p></li>
    <li class="practice-item"><h3>Conveyancing</h3><p>Advice, Buying and Selling Property, Contracts, Settlements, Off the Plan Purchases</p></li>
    <li class="practice-item"><h3>Leases</h3><p>Advice, Commercial and Retail Leases, Industrial Leases, Lease Renewals, Surrender and Assignments of Leases</p></li>
    <li class="practice-item"><h3>Criminal Law</h3><p>Advice, Court Appearances, Pleas, Sentencing, Bail Applications, Driving Offences, Drug Offences, Indictable Offences</p></li>
    <li class="practice-item"><h3>Family Law</h3><p>Advice, Prenuptial Agreements, Divorce Applications, Property Settlements, Parenting Plans, Child Support, Mediation</p></li>
    <li class="practice-item"><h3>Litigation and Dispute Resolution</h3><p>Advice, Commercial Disputes, Civil Disputes, Construction Disputes, Debt Recovery and Lease Disputes, Dispute Resolution, Consumer Claims</p></li>
    <li class="practice-item"><h3>Company Law</h3><p>Advice, Buying and Selling Businesses, Structuring, Incorporation, Shareholder Agreements, Confidentiality, Company Acquisitions</p></li>
    <li class="practice-item"><h3>Wills and Estates</h3><p>Advice, Will Interpretation, Estate Administration, Disputed Wills, Probate</p></li>
    <li class="practice-item"><h3>Powers of Attorney and Guardianship</h3><p>Advice, Drafting Powers of Attorney, Drafting Guardianship Appointments</p></li>
  </ul>
  <footer class="contact-footer">
    <div>
      <div class="firm-name">Prestwicks Solicitors</div>
      <div class="address">3/82 Carradine Street,<br>Liverpool, NSW 2170</div>
    </div>
    <div class="lines">
      <div class="phone">Phone: <strong>(02) 9418 3562</strong></div>
      <div>www.prestwickssolicitors-example.com.au</div>
      <div>info@prestwickssolicitors-example.com.au</div>
    </div>
  </footer>
</section>

<section class="flyer flyer--front">
  <header class="brand-header">
    <div class="brand-name">Prestwicks<span>Solicitors</span></div>
  </header>
  <div class="hero-photo" role="img" aria-label="Black and white photograph of law books and papers on a desk"></div>
  <h1 class="hero-band">Established for <strong>over 30 years,</strong><br>you can <strong>feel confident</strong> with our team</h1>
  <div class="intro">
    <p>Prestwicks Solicitors is a private law firm based in Liverpool that has been servicing the Sydney area for over 30 years. With a dedicated, professional and friendly team we pride ourselves on delivering an exceptional legal service to our clients.</p>
    <p class="tagline">Offering a complete legal service at affordable rates, our clients really do come first.</p>
  </div>
  <footer class="contact-footer">
    <div>
      <div class="firm-name">Prestwicks Solicitors</div>
      <div class="address">3/82 Carradine Street,<br>Liverpool, NSW 2170</div>
    </div>
    <div class="lines">
      <div class="phone">Phone: <strong>(02) 9418 3562</strong></div>
      <div>www.prestwickssolicitors-example.com.au</div>
      <div>info@prestwickssolicitors-example.com.au</div>
    </div>
  </footer>
</section>

</body>
</html>
```